SnackHarbor!!! A Vending Machine Business Looking for an attractive website.

We are a vending machine business in Northern Michigan. We have changed our name and have rebranded our company. We would like an attractive website that shares who we are, what services we provide, the products we offer in our machines, along with a form businesses can fill out to see if they are a good fit for our company. I would like to have a Home Page, About SnackHarbor, Why Choose SnackHarbor?, Products & Services, Contact Us (With a Login Option), and a page with a questionnaire for thos interested in getting a FREE Vending Machine.

Target Market(s)

Businesses, Campgrounds, Schools, and many more in Northern Michigan

Industry/Entity Type

Vending Machines

Number of Pages Required

5+ page

Requirements
Must have
• An inviting and enticing Home Page. I want to get my potential clients engaged in our website.
Nice to have
• Possibly background photos from Northern Michigan
Should not have
• A corporate feel. I do not want a boring website.

```html
<!DOCTYPE html>
<html lang="en">
<head>
<meta charset="utf-8">
<title>SnackHarbor — Elevating Snacking, One Vend at a Time</title>
<link href="https://fonts.googleapis.com/css2?family=Poppins:wght@300;400;500;600;700;800&display=swap" rel="stylesheet">
<style>
:root{
  --navy:#1f1f5c;
  --navy-deep:#181850;
  --green:#3f7a36;
  --green-dark:#2f6229;
  --white:#ffffff;
  --ink:#111111;
  --muted:#7a7a7a;
  --field:#ecefe9;
  --card-shadow:0 6px 18px rgba(0,0,0,.12);
}
*{margin:0;padding:0;box-sizing:border-box}
html,body{width:1200px;height:5302px;overflow:hidden;background:var(--white)}
body{font-family:'Poppins',sans-serif;color:var(--ink)}
.page{position:relative;width:1200px;height:5302px;overflow:hidden}
.abs{position:absolute}
.btn{position:absolute;display:flex;align-items:center;justify-content:center;background:var(--green);color:var(--white);font-weight:600;border-radius:30px;letter-spacing:.5px}
.wordmark{font-weight:700;color:var(--white);display:flex;align-items:center;gap:10px}
.wordmark .mark{width:14px;height:14px;background:var(--white)}

/* hero */
.hero{position:absolute;left:0;top:0;width:1200px;height:780px;background:linear-gradient(180deg,#5d6a96 0%,#6a7c8e 40%,#7d8a6e 70%,#5f6f5e 100%)}
.hero-overlay{position:absolute;inset:0;background:rgba(40,44,110,.45)}
.nav{position:absolute;top:62px;left:342px;display:flex;gap:48px;font-size:14px;font-weight:500;color:var(--white)}
.topbar{position:absolute;top:14px;right:80px;display:flex;gap:50px;font-size:15px;color:var(--white);align-items:center}
.topbar span{display:flex;align-items:center;gap:8px}
.hero h1{position:absolute;top:248px;width:1200px;text-align:center;font-size:70px;line-height:82px;font-weight:800;color:var(--white)}
.hero .tagline{position:absolute;top:428px;width:1200px;text-align:center;font-size:26px;font-weight:400;color:var(--white)}
.feature{position:absolute;top:686px;width:236px;height:188px;background:var(--white);border-radius:10px;box-shadow:var(--card-shadow);text-align:center;padding-top:16px}
.feature h3{font-size:13px;font-weight:700;margin-top:12px}
.feature p{font-size:10.5px;color:var(--muted);line-height:15px;margin:8px 18px 0}

/* about */
.photo-circle{position:absolute;border-radius:50%}
.section-title{font-weight:800;font-size:36px}
.about-text{position:absolute;left:558px;top:1132px;width:560px;font-size:16px;line-height:26px;color:#6b6b6b}

/* who */
.who-text{position:absolute;left:70px;top:1838px;width:580px;font-size:16px;line-height:26px;color:var(--white)}

/* products */
.product{position:absolute;width:280px;height:346px;background:var(--white);border-radius:30px;box-shadow:var(--card-shadow);text-align:center}
.product .photo-circle{left:52px;top:16px;width:176px;height:176px}
.product h3{position:absolute;top:228px;width:100%;font-size:26px;font-weight:600}
.product .go{position:absolute;left:118px;bottom:-22px;width:44px;height:44px;border-radius:8px;background:var(--green);display:flex;align-items:center;justify-content:center}

/* why */
.why-item h3{font-size:28px;font-weight:600;color:var(--white);line-height:30px}
.why-item p{font-size:13px;line-height:20px;color:#dcdcf0;margin-top:6px}

/* form */
.form-panel{position:absolute;left:541px;top:4013px;width:526px;height:648px;background:var(--white);box-shadow:var(--card-shadow)}
.form-panel h2{position:absolute;top:36px;left:122px;font-size:28px;line-height:30px;font-weight:600}
.field{position:absolute;width:204px;height:32px;background:var(--field);border-radius:16px;font-size:8px;color:#777;padding:11px 18px;text-transform:uppercase}

/* footer */
.foot-head{position:absolute;top:4928px;font-size:17px;font-weight:600;color:var(--white)}
.foot-link{position:absolute;font-size:15px;color:var(--white);display:flex;align-items:center;gap:12px}
.foot-link i{width:9px;height:9px;border-radius:50%;background:var(--green);display:block}
</style>
</head>
<body>
<div class="page">

  <!-- HERO -->
  <header class="hero">
    <div class="abs" role="img" aria-label="Aerial view of a Northern Michigan harbor town with white houses, trees and a lighthouse" style="inset:0"></div>
    <div class="hero-overlay"></div>
    <div class="wordmark abs" style="left:22px;top:36px;font-size:40px"><span class="mark"></span>SnackHarbor</div>
    <div class="topbar">
      <span><svg width="18" height="18" viewBox="0 0 24 24"><path fill="#fff" d="M6.6 10.8a15 15 0 0 0 6.6 6.6l2.2-2.2a1 1 0 0 1 1-.25 11 11 0 0 0 3.6.6 1 1 0 0 1 1 1V20a1 1 0 0 1-1 1A17 17 0 0 1 3 4a1 1 0 0 1 1-1h3.5a1 1 0 0 1 1 1 11 11 0 0 0 .6 3.6 1 1 0 0 1-.25 1z"/></svg>(231) 555 0148</span>
      <span><svg width="24" height="24" viewBox="0 0 24 24"><circle cx="12" cy="12" r="11" fill="#fff"/><circle cx="12" cy="9" r="4" fill="#5a5f8c"/><path d="M5 19a8 8 0 0 1 14 0" fill="#5a5f8c"/></svg>LOGIN</span>
    </div>
    <nav class="nav"><span>HOME</span><span>ABOUT</span><span>WHY CHOOSE US</span><span>PRODUCT &amp; SERVICES</span></nav>
    <div class="btn" style="left:946px;top:52px;width:220px;height:38px;font-size:11px;border:2px solid #fff">GET MY FREE VENDING MACHINE</div>
    <h1>ELEVATE YOUR<br>SNACK GAME!</h1>
    <p class="tagline">ELEVATING SNACKING, ONE VEND AT A TIME</p>
    <div class="btn" style="left:508px;top:492px;width:210px;height:48px;font-size:16px;border:2px solid #fff">GET A QUOTE</div>
  </header>
  <svg class="abs" style="left:0;top:620px" width="1200" height="180" viewBox="0 0 1200 180">
    <path d="M0,120 Q600,-60 1200,120 L1200,180 L0,180Z" fill="#fff"/>
    <path d="M0,110 Q600,-70 1200,110" fill="none" stroke="#3f7a36" stroke-width="12"/>
  </svg>

  <div class="feature" style="left:206px">
    <svg width="44" height="64" viewBox="0 0 44 64"><rect x="4" y="2" width="36" height="58" fill="none" stroke="#222" stroke-width="2.5"/><path d="M10 12h16M10 22h16M10 32h16M10 42h16M32 12v30" stroke="#222" stroke-width="2"/><rect x="10" y="50" width="20" height="6" fill="none" stroke="#222" stroke-width="2"/></svg>
    <h3>FLAVOR ARCHITECTS</h3>
    <p>We are architects, community connectors, and taste trailblazers.</p>
  </div>
  <div class="feature" style="left:494px">
    <svg width="64" height="64" viewBox="0 0 64 64"><rect x="14" y="4" width="36" height="40" fill="none" stroke="#222" stroke-width="2.5"/><rect x="6" y="44" width="52" height="16" fill="none" stroke="#222" stroke-width="2.5"/><path d="M20 14h24M20 24h24M20 34h24" stroke="#222" stroke-width="2"/></svg>
    <h3>TAILORED TEMPTATIONS</h3>
    <p>Unwrap joy with nostalgic favorites and exotic treats</p>
  </div>
  <div class="feature" style="left:782px">
    <svg width="52" height="64" viewBox="0 0 52 64"><rect x="3" y="2" width="46" height="58" fill="none" stroke="#222" stroke-width="2.5"/><path d="M9 10h24v40H9zM9 20h24M9 30h24M9 40h24M39 12h6M39 20h6M39 28h6" fill="none" stroke="#222" stroke-width="2"/></svg>
    <h3>SMART AND SEAMLESS</h3>
    <p>Our tech-driven convenience ensures that snacking is smart and seamless.</p>
  </div>

  <!-- ABOUT -->
  <div class="photo-circle" role="img" aria-label="Glass-front drink vending machine stocked with bottled sodas and energy drinks" style="left:68px;top:990px;width:432px;height:432px;background:radial-gradient(circle,#c04a3a 0%,#3a3a44 45%,#1b1b20 70%,#111 100%)"></div>
  <h2 class="section-title abs" style="left:552px;top:1068px">ABOUT SNACKHARBOR</h2>
  <p class="about-text">At SnackHarbor, we don't just vend snacks—we curate cravings. Our customized vending solutions bring flavor, convenience, and community to Northern Michigan. Whether you're reaching for a mid-morning snack, a refreshing beverage, or a satisfying breakfast burrito, SnackHarbor delivers delight with every bite.</p>
  <div class="btn" style="left:570px;top:1292px;width:210px;height:46px;font-size:16px">GET A QUOTE</div>

  <!-- WHO WE ARE -->
  <svg class="abs" style="left:0;top:1500px" width="1200" height="760" viewBox="0 0 1200 760">
    <path d="M0,150 Q600,-80 1200,150 L1200,748 L0,748Z" fill="#1f1f5c"/>
    <path d="M0,128 Q600,-100 1200,128" fill="none" stroke="#3f7a36" stroke-width="12"/>
  </svg>
  <h2 class="abs" style="left:66px;top:1772px;font-size:34px;font-weight:700;color:#fff">WHO WE ARE</h2>
  <p class="who-text">Welcome to SnackHarbor, where snacking meets delight! We're not just about vending machines;we're your culinary companions, your flavor curators, and your secret stash of happiness. Mara and Owen, the dynamic duo behind SnackHarbor, have a passion for all things tasty. With backgrounds in sales and a penchant for personal connections, they've transformed the vending experience into an art form.</p>
  <div class="btn" style="left:70px;top:2042px;width:212px;height:48px;font-size:16px">GET A QUOTE</div>
  <div class="photo-circle" role="img" aria-label="Two side-by-side snack vending machines filled with chips and candy" style="left:690px;top:1698px;width:434px;height:434px;background:radial-gradient(circle,#d85a3a 0%,#3b6bb0 40%,#2a2a30 70%,#e8e8e8 100%)"></div>

  <!-- PRODUCTS -->
  <div class="product" style="left:95px;top:2391px"><div class="photo-circle" role="img" aria-label="Snack vending shelves with chips" style="background:radial-gradient(circle,#e07a30,#b33a2a 50%,#2b2b2b)"></div><h3>SNACKS</h3><div class="go"><svg width="22" height="22" viewBox="0 0 24 24"><circle cx="12" cy="12" r="11" fill="#fff"/><path d="M8 12h7M12 8l4 4-4 4" stroke="#3f7a36" stroke-width="2.5" fill="none"/></svg></div></div>
  <div class="product" style="left:447px;top:2391px"><div class="photo-circle" role="img" aria-label="Drink vending machine with bottled beverages" style="background:radial-gradient(circle,#c8d8e8,#3a6aa8 50%,#222)"></div><h3>DRINKS</h3><div class="go"><svg width="22" height="22" viewBox="0 0 24 24"><circle cx="12" cy="12" r="11" fill="#fff"/><path d="M8 12h7M12 8l4 4-4 4" stroke="#3f7a36" stroke-width="2.5" fill="none"/></svg></div></div>
  <div class="product" style="left:798px;top:2391px"><div class="photo-circle" role="img" aria-label="Frozen food vending machine with meals" style="background:radial-gradient(circle,#c9b48a,#3b4a6a 55%,#1a1a22)"></div><h3>FROZEN</h3><div class="go"><svg width="22" height="22" viewBox="0 0 24 24"><circle cx="12" cy="12" r="11" fill="#fff"/><path d="M8 12h7M12 8l4 4-4 4" stroke="#3f7a36" stroke-width="2.5" fill="none"/></svg></div></div>
  <div class="product" style="left:111px;top:2803px"><div class="photo-circle" role="img" aria-label="Coffee machine drink selection on a dark panel" style="background:radial-gradient(circle,#6a4030,#2a1a18 60%,#0e0a0a)"></div><h3>COFFEE</h3><div class="go"><svg width="22" height="22" viewBox="0 0 24 24"><circle cx="12" cy="12" r="11" fill="#fff"/><path d="M8 12h7M12 8l4 4-4 4" stroke="#3f7a36" stroke-width="2.5" fill="none"/></svg></div></div>
  <div class="product" style="left:463px;top:2803px"><div class="photo-circle" role="img" aria-label="Combination snack and drink vending machines" style="background:radial-gradient(circle,#b85a3a,#44444c 55%,#d8d8d8)"></div><h3>COMBINATION</h3><div class="go"><svg width="22" height="22" viewBox="0 0 24 24"><circle cx="12" cy="12" r="11" fill="#fff"/><path d="M8 12h7M12 8l4 4-4 4" stroke="#3f7a36" stroke-width="2.5" fill="none"/></svg></div></div>
  <div class="product" style="left:815px;top:2803px"><div class="photo-circle" role="img" aria-label="Custom stocked vending machine with mixed products" style="background:radial-gradient(circle,#e0a040,#3b6bb0 50%,#2a2a2a)"></div><h3>CUSTOM</h3><div class="go"><svg width="22" height="22" viewBox="0 0 24 24"><circle cx="12" cy="12" r="11" fill="#fff"/><path d="M8 12h7M12 8l4 4-4 4" stroke="#3f7a36" stroke-width="2.5" fill="none"/></svg></div></div>

  <!-- WHY CHOOSE US -->
  <svg class="abs" style="left:0;top:3266px" width="1200" height="630" viewBox="0 0 1200 630">
    <path d="M0,0 H1200 V510 Q600,640 0,510Z" fill="#1f1f5c"/>
    <path d="M0,545 Q600,680 1200,545" fill="none" stroke="#3f7a36" stroke-width="12"/>
  </svg>
  <h2 class="abs" style="top:3322px;width:1150px;text-align:center;font-size:36px;font-weight:700;color:#fff">WHY CHOOSE US</h2>

  <svg class="abs" style="left:38px;top:3430px" width="82" height="74" viewBox="0 0 82 74"><path d="M41 70 C10 48 3 34 3 22 A18 18 0 0 1 41 14 A18 18 0 0 1 79 22 C79 34 72 48 41 70Z" fill="none" stroke="#fff" stroke-width="3"/></svg>
  <div class="why-item abs" style="left:146px;top:3398px;width:400px"><h3>Local Love</h3><p>We celebrate the heart of Michigan by partnering with local legends. Say hello to Pinecrest Jerky and Lakeshore Kettle Chips—our hometown heroes. Their flavors dance on your taste buds, and we're thrilled to bring them straight to your workplace.</p></div>

  <svg class="abs" style="left:624px;top:3444px" width="74" height="92" viewBox="0 0 74 92"><path d="M37 4l4 8 9 1-7 6 2 9-8-5-8 5 2-9-7-6 9-1z" fill="none" stroke="#fff" stroke-width="2.5"/><path d="M10 26l2 5 5 .5-4 3.5 1 5-4-3-4 3 1-5-4-3.5 5-.5zM64 26l2 5 5 .5-4 3.5 1 5-4-3-4 3 1-5-4-3.5 5-.5z" fill="none" stroke="#fff" stroke-width="2"/><rect x="8" y="52" width="12" height="36" fill="none" stroke="#fff" stroke-width="2.5"/><path d="M20 56 L32 40 Q38 36 38 46 L36 54 H60 Q66 56 62 62 Q66 66 60 70 Q64 76 58 78 Q60 86 52 86 H20Z" fill="none" stroke="#fff" stroke-width="2.5"/></svg>
  <div class="why-item abs" style="left:730px;top:3422px;width:430px"><h3>Unleash Your Cravings</h3><p>SnackHarbor isn't bound by corporate ties. We're the rebels of the vending world. Cravings bag of crispy, kettle-cooked chips? Done. Hankering for jerky that packs a punch? We've got you covered. Our machines are like treasure chests, waiting for you to unlock flavor magic.</p></div>

  <svg class="abs" style="left:50px;top:3644px" width="74" height="94" viewBox="0 0 74 94"><circle cx="37" cy="34" r="30" fill="none" stroke="#fff" stroke-width="3"/><circle cx="37" cy="34" r="20" fill="none" stroke="#fff" stroke-width="2.5"/><path d="M37 22l3.5 7 7.5 1-5.5 5 1.5 7.5-7-4-7 4 1.5-7.5-5.5-5 7.5-1z" fill="none" stroke="#fff" stroke-width="2"/><path d="M18 58 L8 88 L20 82 L26 92 L32 66M56 58 L66 88 L54 82 L48 92 L42 66" fill="none" stroke="#fff" stroke-width="2.5"/></svg>
  <div class="why-item abs" style="left:146px;top:3598px;width:420px"><h3>Quality Meets Convenience</h3><p>Imagine this: You're mid-meeting, and your stomach growls. Fear not! SnackHarbor's machines offer top-notch snacks and beverages. It's like having a mini food festival at your fingertips.</p></div>

  <svg class="abs" style="left:642px;top:3640px" width="52" height="84" viewBox="0 0 52 84"><rect x="3" y="3" width="46" height="78" rx="3" fill="none" stroke="#fff" stroke-width="3"/><path d="M10 12h22v50H10zM10 24h22M10 36h22M10 48h22M38 14h6M38 22h6M38 30h6M12 70h28" fill="none" stroke="#fff" stroke-width="2.2"/></svg>
  <div class="why-item abs" style="left:730px;top:3610px;width:440px"><h3>Pandemic-Proof &amp;<br>Recession-Ready</h3><p>Life throws curveballs, but SnackHarbor stands strong. Our vending machines are the unsung heroes of resilience. Rain or shine, they're there, serving up joy</p></div>

  <!-- FREE MACHINE FORM -->
  <div class="abs" role="img" aria-label="Close-up of a snack vending machine filled with colorful chip bags" style="left:93px;top:4013px;width:448px;height:648px;background:linear-gradient(180deg,#c84a2e 0%,#e0a03a 20%,#3f7ac0 40%,#b93a34 60%,#e8c04a 72%,#c8c8c8 82%,#dedede 100%)"></div>
  <section class="form-panel">
    <h2>Interested in getting a<br>FREE Vending Machine</h2>
    <div class="field" style="left:48px;top:114px">Employees</div>
    <div class="field" style="left:286px;top:114px">Check all that apply (open)</div>
    <div class="field" style="left:48px;top:174px">What county</div>
    <div class="field" style="left:286px;top:174px">Type of business</div>
    <div class="field" style="left:48px;top:234px">Do you currently have vending?</div>
    <div class="field" style="left:286px;top:234px">What type of vending are you interested in?</div>
    <div class="field" style="left:48px;top:294px">When would you like to start</div>
    <div class="field" style="left:286px;top:294px">Business name</div>
    <div class="field" style="left:48px;top:354px">Contact person</div>
    <div class="field" style="left:286px;top:354px">Contact phone number</div>
    <div class="field" style="left:48px;top:414px">Contact email</div>
    <div class="field" style="left:286px;top:414px">Best time to call</div>
    <div class="field" style="left:48px;top:474px;width:442px;height:82px;padding-top:34px">Message</div>
    <div class="btn" style="left:121px;top:588px;width:306px;height:38px;font-size:12px">GET MY FREE VENDING MACHINE</div>
  </section>

  <!-- FOOTER -->
  <svg class="abs" style="left:0;top:4800px" width="1200" height="502" viewBox="0 0 1200 502">
    <path d="M0,95 Q600,-40 1200,95 V502 H0Z" fill="#1f1f5c"/>
    <path d="M0,80 Q600,-58 1200,80" fill="none" stroke="#3f7a36" stroke-width="10"/>
  </svg>
  <div class="wordmark abs" style="left:66px;top:4934px;font-size:44px"><span class="mark"></span>SnackHarbor</div>
  <p class="abs" style="left:64px;top:5030px;width:360px;font-size:17px;line-height:26px;color:#fff">A Leader Among Aging-in-Place Home Remodeling Companiesers</p>
  <div class="abs" style="left:64px;top:5118px;display:flex;gap:30px">
    <span style="width:24px;height:24px;border-radius:50%;background:var(--green)"></span>
    <span style="width:24px;height:24px;border-radius:50%;background:var(--green)"></span>
    <span style="width:24px;height:24px;border-radius:50%;background:var(--green)"></span>
  </div>

  <h4 class="foot-head" style="left:456px">QUICK LINKS</h4>
  <div class="foot-link" style="left:458px;top:4976px"><i></i>HOME</div>
  <div class="foot-link" style="left:458px;top:5016px"><i></i>ABOUT</div>
  <div class="foot-link" style="left:458px;top:5056px"><i></i>WHO WE ARE</div>
  <div class="foot-link" style="left:458px;top:5096px"><i></i>SERVICES</div>
  <div class="foot-link" style="left:458px;top:5136px"><i></i>CONTACT</div>

  <h4 class="foot-head" style="left:660px">CONTACT INFO</h4>
  <div class="foot-link" style="left:662px;top:5054px"><svg width="24" height="18" viewBox="0 0 24 18"><rect width="24" height="18" rx="2" fill="#3f7a36"/><path d="M2 3l10 7 10-7" stroke="#1f1f5c" stroke-width="2" fill="none"/></svg>hello@snackharbor.example</div>
  <div class="foot-link" style="left:666px;top:5100px"><svg width="18" height="26" viewBox="0 0 18 26"><path d="M9 1a8 8 0 0 1 8 8c0 6-8 16-8 16S1 15 1 9a8 8 0 0 1 8-8z" fill="#3f7a36"/><circle cx="9" cy="9" r="3" fill="#1f1f5c"/></svg>214 Bayview Rd, Petoskey</div>

  <h4 class="foot-head" style="left:938px">SIGNUP NOW</h4>
  <p class="abs" style="left:938px;top:4992px;width:240px;font-size:8px;line-height:11px;color:#fff">Sign up now and let's connect. Taste the future of snacking firsthand! Contact us today and explore how our vending magic can elevate your space.</p>
  <div class="btn" style="left:938px;top:5056px;width:178px;height:40px;font-size:14px;border-radius:4px">CONTACT US</div>

  <p class="abs" style="left:96px;top:5250px;font-size:12px;color:#fff">© Copyright 2024 - SnackHarbor. All Rights Reserved.</p>
  <p class="abs" style="left:916px;top:5250px;font-size:12px;color:#fff">Privacy Policy | Terms and Conditions</p>

</div>
</body>
</html>
```